Creation of a Facebook cover graphic

We need a Facebook cover graphic for a page that will be used to test the market for an online training product.

The Product

The subject of the training is the basic online marketing. The training will be delivered online rather than at a venue.

The name of the website is www.tallowfinchhub.com. PLEASE NOTE We have owned the site domain for a while and the current content is 'NOT' representative of the new product. If Quillbarrow deliver on this project we will be back for the website and logo designs! please note we have included a draft logo concept file attachment with the brief.

Design Details

The cover graphic will be viewed on desktop, tablet and mobile. We have tried to give you a brief that guarantees the profile looks good and is readable on mobile. The design is bold and simple in order to enhance viewing the graphic on mobile.

We have included a draft graphic (Both as psd and png). This only shows layout and content. The draft graphic is mainly text based.

We have also included a concept file for the logo. You may want to incorporate the target and arrow icon contained in that file into the design.

Creating a design optimised for mobile is perhaps more challenging than larger formats. Feel free to designs with the following elements: Backgrounds; shapes; gradients and font/text effects - however try and retain a flat and simple design

Graphic size: 828px x 315px – we prefer this size rather than the mobile specific size. It actually renders best across all devices.
Place the design in between 174px & 650px horizontally as this gives best viewing on mobile. Backgrounds can extend across the whole graphic.
Web resolution

There are 2 section to the design:

Section 1. Title ‘The Bright Harbour Crew’
Section 2. Sub title ’Solving online marketing needs’ and to do listing

For the logo colouring and background we would prefer:

Background colour: #236d99 will be our main corporate colour. Other colours are #00456e, #236d99 and # 82bcd0.
Text colour : white or white with a shade of blue. You may contrast text colour of section 1 and section 2.

Fonts : We have two font styles in the draft (Arial Black and Arial Nova). The mobile first design requires the fonts to be very simple so as the text can be read on mobile devices. You can try similar such as Helvetica, Lato etc.
Icons etc : There are 3 ticks against each element of the to do list. Feel free to creative how you want to work with these.

Examples

The Quillbarrow graphic included in the files is a good example of simplicity and flat design.

Target Market(s)

Our clients will be business owners and managers. Generally, one person, small and medium sized businesses.
Gender : Both male and female.
Typical ages : 35-65
They favour simplicity, functionality and boldness - rather than elegance or sophistication

Industry/Entity Type

Marketing

Font styles to use
Sans Serif

Requirements
Must have
• View well on mobile devices
• Text readable on mobile devices
• Simplicity
• Flatter type of design
Nice to have
• Not really a design idea. Would like some feedback on whether our design brief was useful for you as designers.
Should not have
• Complex and finely detailed design

```html
<!DOCTYPE html>
<html lang="en">
<head>
<meta charset="utf-8">
<title>The Bright Harbour Crew – Cover</title>
<link href="https://fonts.googleapis.com/css2?family=Quicksand:wght@500;700&display=swap" rel="stylesheet">
<style>
  :root {
    --page-bg: #222222;
    --cover-blue: #2e3f93;
    --pattern-blue: #2c3c8e;
    --text-white: #ffffff;
    --tick-teal: #3cc7c0;
  }
  html, body {
    margin: 0;
    padding: 0;
    width: 1200px;
    height: 1200px;
    overflow: hidden;
    background: var(--page-bg);
  }
  .cover {
    position: absolute;
    left: 0;
    top: 372px;
    width: 1200px;
    height: 456px;
    background: var(--cover-blue);
    overflow: hidden;
    font-family: "Quicksand", sans-serif;
    color: var(--text-white);
  }
  .icon-pattern {
    position: absolute;
    inset: 0;
    background: var(--pattern-blue);
  }
  .headline {
    position: absolute;
    left: 0;
    width: 100%;
    text-align: center;
    margin: 0;
  }
  .headline--title {
    top: 82px;
    font-size: 50px;
    font-weight: 700;
    letter-spacing: 2px;
    line-height: 1;
  }
  .headline--subtitle {
    top: 140px;
    font-size: 34px;
    font-weight: 700;
    letter-spacing: 1.6px;
    line-height: 1;
  }
  .benefit-list {
    position: absolute;
    left: 370px;
    top: 190px;
    margin: 0;
    padding: 0;
    list-style: none;
  }
  .benefit {
    display: flex;
    align-items: center;
    height: 46px;
    font-size: 36px;
    font-weight: 500;
    letter-spacing: 1.8px;
  }
  .benefit svg {
    width: 36px;
    height: 36px;
    margin-right: 13px;
    flex: none;
  }
  .brand-name {
    position: absolute;
    left: 848px;
    top: 370px;
    margin: 0;
    font-size: 20px;
    font-weight: 700;
    letter-spacing: 0.5px;
    line-height: 1;
    color: var(--text-white);
  }
</style>
</head>
<body>
  <section class="cover">
    <div class="icon-pattern" role="img" aria-label="Faint pattern of outlined online marketing icons"></div>

    <h1 class="headline headline--title">The Bright Harbour Crew</h1>
    <h2 class="headline headline--subtitle">Solving Online Marketing Needs</h2>

    <ul class="benefit-list">
      <li class="benefit">
        <svg viewBox="0 0 36 36" aria-hidden="true"><circle cx="18" cy="18" r="17" fill="var(--tick-teal)"/><path d="M10 18.5l5.5 5.5L26.5 13" fill="none" stroke="#fff" stroke-width="3" stroke-linecap="round" stroke-linejoin="round"/></svg>
        Making web sites “sticky”
      </li>
      <li class="benefit">
        <svg viewBox="0 0 36 36" aria-hidden="true"><circle cx="18" cy="18" r="17" fill="var(--tick-teal)"/><path d="M10 18.5l5.5 5.5L26.5 13" fill="none" stroke="#fff" stroke-width="3" stroke-linecap="round" stroke-linejoin="round"/></svg>
        Increasing conversions
      </li>
      <li class="benefit">
        <svg viewBox="0 0 36 36" aria-hidden="true"><circle cx="18" cy="18" r="17" fill="var(--tick-teal)"/><path d="M10 18.5l5.5 5.5L26.5 13" fill="none" stroke="#fff" stroke-width="3" stroke-linecap="round" stroke-linejoin="round"/></svg>
        Boosting quality traffic
      </li>
    </ul>

    <p class="brand-name">Tallow Finch Hub</p>
  </section>
</body>
</html>
```